Northwind Crown Hair Supply needs a packaging design

We need a packaging design for a new hair extension company based in Edmonton, Alberta called Velvet Strands. Our packaging should communicate high quality, luxurious hair that will never tangle or dry out. The product will be marketed to salon professionals as well as clients. There must be an opening to see the hair from the outside.

Our advertising campaign is going to be based on boho chic; Dorian Keswick/ Open Meadow/Tumbling Echo.

Target Market(s)

Women and beauty industry professionals. High end market.

Industry/Entity Type

Advertising

Requirements
Must have
• "Highest quality 100% Remi hair!" should be written on the front of the package. In addition, we would like to add text to the back or inside of the packaging as follows:
• Hair Collection and Color Processing:
• Only the highest quality hair is selected which ensures high moisture and nutrient content
• The hair is directly cut from the donor which ensures that the hair cuticle remains intact and always tangle-free
• No chemicals are used in dyeing the hair
• The hair will never fade due to the mild and healthy herbal extract used in the dyeing process which gently penetrates to the inner core of the hair
• Care Instructions:
• Velvet Strands provides only the highest in quality Remi hair that demands very little care to maintain it’s luxurious feel.
• Use a proper extension bristle brush
• Wash the hair with a sulfate-free shampoo and follow with a moisturizing conditioner that is formulated for hair extensions
• Do not apply any type of chemicals to the hair
• We proudly show our immense passion for delivering superior quality in our full product line.
• We insist that it is important for you to know and understand what you are purchasing in your hair extensions. We guarantee the highest quality of our products.
• Velvet Strands is strongly committed to serving their clients with utmost integrity, believing in a foundation of personal and professional ethics and our 20 years service in the beauty industry.

```html
<!DOCTYPE html>
<html lang="en">
<head>
<meta charset="utf-8">
<title>Velvet Strands – Packaging</title>
<link rel="stylesheet" href="https://fonts.googleapis.com/css2?family=Alegreya:wght@400;500&display=swap">
<style>
  :root {
    --backdrop: #f1e6dc;
    --box-black: #141211;
    --panel-black: #1b1918;
    --gold: #d9b46c;
    --gold-soft: #b8924f;
    --pattern-dark: #1a1816;
    --pattern-mid: #2c2620;
  }
  * { box-sizing: border-box; margin: 0; padding: 0; }
  html, body {
    width: 1200px;
    height: 1000px;
    overflow: hidden;
    background: var(--backdrop);
    font-family: "Alegreya", Georgia, serif;
  }
  .canvas {
    position: relative;
    width: 1200px;
    height: 1000px;
  }
  .package {
    position: absolute;
    left: 300px;
    top: 60px;
    display: flex;
    height: 900px;
  }
  .panel {
    position: relative;
    height: 100%;
    background: var(--box-black);
    overflow: hidden;
  }
  .panel-side { width: 310px; border-right: 1px solid #2a2522; }
  .panel-front { width: 420px; }
  .wave-pattern {
    position: absolute;
    inset: 0;
    background:
      linear-gradient(100deg, var(--pattern-dark) 0%, var(--pattern-mid) 35%, var(--pattern-dark) 55%, var(--pattern-mid) 80%, var(--pattern-dark) 100%);
  }
  .info-box {
    position: absolute;
    left: 28px;
    right: 28px;
    top: 14px;
    bottom: 14px;
    background: var(--panel-black);
    border: 1.5px solid var(--gold);
    outline: 1px solid var(--gold-soft);
    outline-offset: -6px;
    padding: 28px 22px;
    color: var(--gold);
    text-align: center;
    font-size: 13.6px;
    line-height: 1.32;
  }
  .info-box p { margin-bottom: 13px; }
  .info-box .section-title {
    font-weight: 500;
    letter-spacing: 0.06em;
    margin: 4px 0 13px;
  }
  .front-branding {
    position: absolute;
    left: 190px;
    top: 250px;
    height: 420px;
    display: flex;
    gap: 22px;
    transform: rotate(180deg);
  }
  .brand-name,
  .tagline {
    writing-mode: vertical-rl;
    color: var(--gold);
    white-space: nowrap;
  }
  .brand-name {
    font-size: 42px;
    font-weight: 500;
    letter-spacing: 0.04em;
    align-self: center;
  }
  .tagline {
    font-size: 24px;
    font-weight: 400;
    letter-spacing: 0.02em;
    align-self: flex-start;
  }
</style>
</head>
<body>
<main class="canvas">
  <div class="package">
    <section class="panel panel-side">
      <div class="wave-pattern" role="img" aria-label="Flowing gold hair-strand line pattern on black"></div>
      <div class="info-box">
        <p>Only the highest quality hair is selected which ensures high moisture and nutrient content</p>
        <p>The hair is directly cut from the donor which ensures that the hair cuticle remains intact and always tangle-free</p>
        <p>No chemicals are used in dyeing the hair</p>
        <p>The hair will never fade due to the mild and healthy herbal extract used in the dyeing process which gently penetrates to the inner core of the hair</p>
        <p class="section-title">CARE INSTRUCTIONS</p>
        <p>Use a proper extension bristle brush</p>
        <p>Wash the hair with a sulfate-free shampoo and follow with a moisturizing conditioner that is formulated for hair extensions</p>
        <p>Do not apply any type of chemicals to the hair</p>
        <p>We proudly show our immense passion for delivering superior quality in our full product line</p>
        <p>We insist that it is important for you to know and understand what you are purchasing in your hair extensions. We guarantee the highest quality of our products.</p>
        <p>Velvet Strands is strongly committed to serving their clients with utmost integrity, believing in a foundation of personal and professional ethics and our 20 years service in the beauty industry.</p>
      </div>
    </section>
    <section class="panel panel-front">
      <div class="wave-pattern" role="img" aria-label="Flowing gold hair-strand line pattern on black"></div>
      <div class="front-branding">
        <span class="tagline">Highest quality 100% Remi hair</span>
        <span class="brand-name">Velvet Strands</span>
      </div>
    </section>
  </div>
</main>
</body>
</html>
```